Harvest Bridge Christian Ministry needs a Conference Ad

We are a Christian nonprofit focused on eliminating systemic poverty and helping believers function as ministers in their workplaces. The 2025 Lantern Path Global Conference coming up in October, and we need an ad for social media (facebook, instagram, and X) and our website in order to get people excited to attend! We are looking for a modern and sleek design that incorporates our logo (attached file). You can either put just the butterfly and then write our company name separately somewhere in the design or use it as is (we used Gotham font for the logo). We want to emphasize the joy of in-person connection at the conference, so you could possibly include stock photos of young people gathering together. You could also include the attached photo of our founders in the design and say “with Mel and Dora Quintavan". Also, include the conference dates, which are October 9-12, 2025, and say “come in person or join online”. Lastly, please include the tagline “from the Pellmore Awakening to Worldwide Transformation”. NOTE: I’m attaching AN EXAMPLE I’ve created of how the design could look, which you can feel free to use for inspiration.
Young people on Instagram and facebook
- Gotham

```html
<!DOCTYPE html>
<html lang="en">
<head>
<meta charset="utf-8">
<title>Lantern Path Global Conference – Ad</title>
<link rel="stylesheet" href="https://fonts.googleapis.com/css2?family=Montserrat:wght@500;600;700;800;900&display=swap">
<style>
  :root {
    --stage: #3b3b3b;
    --paper: #ffffff;
    --ink: #111111;
    --accent-blue: #2b50b8;
    --band-blue: #66a6d9;
    --pill-yellow: #f3c92f;
    --photo-dark: #2a211c;
    --photo-mid: #6b5140;
    --photo-light: #c9a37d;
  }
  * { box-sizing: border-box; margin: 0; padding: 0; }
  html, body {
    width: 825px; height: 1200px; overflow: hidden;
    background: var(--stage);
    font-family: "Montserrat", Arial, sans-serif;
  }
  .ad {
    position: absolute; left: 0; top: 187px;
    width: 825px; height: 825px;
    background: var(--paper);
    overflow: hidden;
  }
  .founders-photo {
    position: absolute; left: 0; top: 0;
    width: 825px; height: 825px;
  }
  .brand {
    position: absolute; left: 100px; top: 96px; width: 250px;
    display: flex; flex-direction: column; align-items: center; gap: 14px;
    color: var(--ink);
  }
  .brand-mark {
    width: 70px; height: 70px; border-radius: 50%;
    background: var(--ink);
  }
  .brand-name {
    font-weight: 500; font-size: 25px; line-height: 1.05;
    text-align: center; letter-spacing: 0.5px; text-transform: uppercase;
  }
  .headline {
    position: absolute; left: 49px; top: 280px;
    font-weight: 900; font-size: 50px; line-height: 53px;
    color: var(--ink); text-transform: uppercase;
  }
  .date-month {
    position: absolute; left: 47px; top: 462px;
    font-weight: 900; font-size: 72px; line-height: 1;
    color: var(--accent-blue); letter-spacing: -1px;
  }
  .date-days {
    position: absolute; left: 99px; top: 530px;
    font-weight: 700; font-size: 52px; line-height: 1;
    color: var(--ink);
  }
  .attend-pill {
    position: absolute; left: 49px; top: 584px;
    width: 462px; height: 36px; border-radius: 14px;
    background: var(--pill-yellow);
    font-weight: 600; font-size: 26px; line-height: 36px;
    text-align: center; color: var(--ink);
  }
  .tagline-band {
    position: absolute; left: 0; top: 741px;
    width: 825px; height: 55px;
    background: var(--band-blue);
    font-weight: 700; font-size: 23px; line-height: 55px;
    text-align: center; color: var(--ink);
  }
</style>
</head>
<body>
  <main class="ad">
    <svg class="founders-photo" viewBox="0 0 825 825" role="img" aria-label="Photo of founders Mel and Dora Quintavan smiling together">
      <defs>
        <linearGradient id="photoTone" x1="0" y1="0" x2="1" y2="1">
          <stop offset="0" stop-color="var(--photo-dark)"/>
          <stop offset="0.45" stop-color="var(--photo-mid)"/>
          <stop offset="0.75" stop-color="var(--photo-light)"/>
          <stop offset="1" stop-color="var(--photo-dark)"/>
        </linearGradient>
      </defs>
      <polygon fill="url(#photoTone)"
        points="427,135 686,0 825,0 825,349 780,353 825,414 743,653 566,706 464,406"/>
    </svg>

    <div class="brand">
      <div class="brand-mark"></div>
      <div class="brand-name">Harvest Bridge</div>
    </div>

    <h1 class="headline">With Mel<br>and Dora<br>Quintavan</h1>
    <p class="date-month">OCTOBER</p>
    <p class="date-days">9-12 2025</p>
    <p class="attend-pill">come in person or join online</p>

    <p class="tagline-band">from the Pellmore Awakening to Worldwide Transformation</p>
  </main>
</body>
</html>
```